professional business card

Professional business card with logo on one side, and underneath logo list:
- power
-data
-fibre optic
-isolar

On other side:
Marcus Webb
Owner
MOB 0432 958 720
marcus@vorn.com.au
www.vornelectrical.com.au

Please edit logo to just leave VORN

```html
<!DOCTYPE html>
<html lang="en">
<head>
<meta charset="utf-8">
<title>VORN Electrical – Business Card</title>
<link href="https://fonts.googleapis.com/css2?family=Lato:wght@400;700;900&display=swap" rel="stylesheet">
<style>
  :root {
    --teal: #32a3a5;
    --teal-deep: #2a8f91;
    --grey-text: #8a8a8a;
    --grey-dark: #7a7a7a;
    --card-white: #f1f1f1;
    --backdrop: #4a4a4a;
    --white: #ffffff;
  }
  * { margin: 0; padding: 0; box-sizing: border-box; }
  html, body {
    width: 1033px; height: 1200px; overflow: hidden;
    background: var(--backdrop);
    font-family: "Lato", sans-serif;
  }
  .card {
    position: absolute; left: 158px; width: 726px; height: 415px;
  }
  .card-front { top: 145px; background: linear-gradient(135deg, #f7f7f7, #e6e6e6); }
  .card-back { top: 634px; background: linear-gradient(160deg, #33a6a8, var(--teal-deep)); }

  .accent-band {
    position: absolute; left: 108px; width: 510px; height: 17px; background: var(--teal);
  }
  .accent-band.top { top: 0; }
  .accent-band.bottom { bottom: 0; }

  .holder-name {
    position: absolute; left: 45px; top: 128px;
    font-size: 38px; font-weight: 400; color: var(--grey-text); line-height: 1;
  }
  .holder-role {
    position: absolute; left: 46px; top: 171px;
    font-size: 19px; letter-spacing: 2px; color: var(--teal); line-height: 1;
  }
  .contact-list { position: absolute; left: 46px; top: 211px; list-style: none; }
  .contact-list li {
    display: flex; align-items: center; height: 25.5px;
    font-size: 17px; letter-spacing: 0.6px; color: var(--grey-text);
  }
  .contact-list svg { width: 19px; height: 19px; margin-right: 12px; flex: none; }

  .brand-block {
    position: absolute; left: 410px; top: 160px; width: 272px; text-align: center;
  }
  .brand-name {
    font-size: 94px; font-weight: 900; color: var(--teal);
    line-height: 78px; letter-spacing: 1px;
  }
  .brand-rule { height: 2px; background: var(--grey-text); margin: 6px 0 8px; }
  .brand-sub {
    font-size: 25px; color: var(--grey-dark); letter-spacing: 12.5px;
    margin-right: -12px; line-height: 1;
  }
  .brand-licence {
    font-size: 18px; color: var(--grey-dark); letter-spacing: 10px;
    margin-top: 8px; line-height: 1; padding-left: 0; margin-right: -10px;
  }

  .services {
    position: absolute; top: 350px; left: 0; width: 726px; text-align: center;
    font-size: 21px; letter-spacing: 3.6px; color: var(--grey-text); line-height: 1;
  }
  .services .sep { margin: 0 6px; }

  .back-brand {
    position: absolute; left: 162px; top: 52px;
    font-size: 86px; font-weight: 900; color: var(--white); line-height: 1; letter-spacing: 1px;
  }
  .back-services {
    position: absolute; left: 162px; top: 332px;
    font-size: 17px; letter-spacing: 3px; color: var(--white); line-height: 1;
  }
  .back-services .sep { margin: 0 5px; }
</style>
</head>
<body>
  <section class="card card-front">
    <div class="accent-band top"></div>
    <div class="accent-band bottom"></div>

    <h1 class="holder-name">Marcus Webb</h1>
    <p class="holder-role">OWNER</p>

    <ul class="contact-list">
      <li>
        <svg viewBox="0 0 20 20" aria-hidden="true"><circle cx="10" cy="10" r="10" fill="#32a3a5"/><rect x="6.5" y="4" width="7" height="12" rx="1.5" fill="none" stroke="#fff" stroke-width="1.6"/><circle cx="10" cy="13.6" r="0.9" fill="#fff"/></svg>
        0432 958 720
      </li>
      <li>
        <svg viewBox="0 0 20 20" aria-hidden="true"><circle cx="10" cy="10" r="10" fill="#32a3a5"/><path d="M5 8.5 L10 5 L15 8.5 V14.5 H5 Z" fill="none" stroke="#fff" stroke-width="1.4" stroke-linejoin="round"/><path d="M5 8.5 L10 12 L15 8.5" fill="none" stroke="#fff" stroke-width="1.4"/></svg>
        marcus@vorn.com.au
      </li>
      <li>
        <svg viewBox="0 0 20 20" aria-hidden="true"><circle cx="10" cy="10" r="10" fill="#32a3a5"/><path d="M5 7 L7.5 13.5 L10 8.5 L12.5 13.5 L15 7" fill="none" stroke="#fff" stroke-width="1.8" stroke-linejoin="round" stroke-linecap="round"/></svg>
        www.vornelectrical.com.au
      </li>
    </ul>

    <div class="brand-block">
      <div class="brand-name">VORN</div>
      <div class="brand-rule"></div>
      <div class="brand-sub">ELECTRICAL</div>
      <div class="brand-licence">EC27390</div>
    </div>

    <p class="services">POWER<span class="sep">|</span>DATA<span class="sep">|</span>FIBRE OPTIC<span class="sep">|</span>ISOLAR</p>
  </section>

  <section class="card card-back">
    <div class="back-brand">VORN</div>
    <p class="back-services">POWER<span class="sep">|</span>DATA<span class="sep">|</span>FIBRE OPTIC<span class="sep">|</span>ISOLAR</p>
  </section>
</body>
</html>
```